QNRV PowerPoint Template for Apartment Association

We are an association of banks that invest equity in low-income housing. I need a PPT template that captures our role in providing housing, but is professional and modern. We aren't the housing developers or owners. We are the banks providing equity. The PPT will be used for a wide variety of virtual and in-person meetings. I have provided our brand guidelines and our current PPT (which we don't love) and a recent conference brochure, which we like more.

I am looking for a versatile PPT template. I would like four options for the cover slide and then only a handful of interior slides. Don't use the brochure to populate it. I am looking for a template, not an actual PPT. Keep it simple!

Colors should be our brand. Light, airy and modern. It would be helpful to have apartment housing incorporated somehow. But not necessarily as a picture of a property. Just visually integrated to connect that the work we do creates housing, but at the end of the day, we are bankers. I am providing some pictures you can use.

Target Market(s)

Financial professionals

Font styles to use
Other font styles liked:
• Use our brand fonts provided in the brand guidelines.

Requirements
Should not have
• people in the pictures

```html
<!DOCTYPE html>
<html lang="en">
<head>
<meta charset="utf-8">
<title>QNRV Cover Slide Options</title>
<link href="https://fonts.googleapis.com/css2?family=Oswald:wght@500;600;700&family=Montserrat:wght@400;600;700&display=swap" rel="stylesheet">
<style>
  :root {
    --orange: #ea7422;
    --orange-soft: rgba(234,116,34,0.55);
    --charcoal: #3b3b3d;
    --charcoal-deep: #2c2c2e;
    --navy: #1c2536;
    --white: #ffffff;
    --paper: #eeeeee;
    --ink: #4a4a4a;
    --muted: #9a9a9a;
  }
  * { box-sizing: border-box; margin: 0; padding: 0; }
  html, body { width: 882px; height: 1200px; overflow: hidden; }
  body {
    background: var(--paper);
    position: relative;
    font-family: "Montserrat", Arial, sans-serif;
  }
  .slide {
    position: absolute;
    width: 386px;
    height: 217px;
    overflow: hidden;
    box-shadow: 0 2px 6px rgba(0,0,0,0.18);
  }
  .col-a { left: 48px; }
  .col-b { left: 448px; }
  .row-1 { top: 30px; }
  .row-2 { top: 322px; }
  .row-3 { top: 614px; }
  .row-4 { top: 906px; }

  .abs { position: absolute; }
  .photo-dusk { background: linear-gradient(160deg, #2a3852 0%, #3a4558 45%, #6b4a34 80%, #3a2a22 100%); }
  .photo-night { background: linear-gradient(150deg, #1d2638 0%, #2b3346 55%, #4a3a30 100%); }
  .photo-day { background: linear-gradient(170deg, #b9c7d6 0%, #8d7a66 55%, #5b4a3e 100%); }
  .photo-dim { background: linear-gradient(150deg, #2f3033 0%, #45403c 60%, #2a2a2c 100%); }
  .shade { background: linear-gradient(90deg, rgba(20,26,38,0.85) 0%, rgba(20,26,38,0.35) 70%, rgba(20,26,38,0.1) 100%); }

  .title {
    font-family: "Oswald", Arial, sans-serif;
    font-weight: 700;
    text-transform: uppercase;
    line-height: 1.02;
    letter-spacing: 0.3px;
  }
  .subtitle {
    font-family: "Montserrat", Arial, sans-serif;
    font-weight: 700;
    text-transform: uppercase;
    font-size: 6.5px;
    letter-spacing: 0.8px;
  }
  .kicker {
    font-size: 5px;
    font-weight: 600;
    letter-spacing: 1.6px;
    text-transform: uppercase;
  }
  .fine { font-size: 4.5px; line-height: 1.5; }
  .orange { color: var(--orange); }
  .white { color: var(--white); }
  .ink { color: var(--ink); }

  .brand {
    display: flex;
    align-items: center;
    gap: 4px;
    font-family: "Oswald", Arial, sans-serif;
    font-weight: 700;
    font-size: 14px;
    letter-spacing: 0.5px;
  }
  .brand-mark { width: 9px; height: 9px; background: var(--orange); }
  .brand-tag { font-size: 3.6px; line-height: 1.3; color: var(--muted); margin-left: 3px; font-family: "Montserrat", Arial, sans-serif; font-weight: 600; }

  .footer-strip {
    left: 0; right: 0; bottom: 0; height: 48px;
    background: var(--white);
    display: flex; align-items: center; justify-content: space-between;
    padding: 0 18px;
  }
  .contact { text-align: left; color: var(--ink); }
  .contact b { color: var(--orange); }

  .info-box {
    border: 1px solid var(--orange);
    padding: 4px 7px;
    color: var(--white);
  }
</style>
</head>
<body>

<!-- Option 1 -->
<section class="slide col-a row-1" style="background:var(--white)">
  <div class="abs photo-dusk" style="left:0;top:0;width:386px;height:169px" role="img" aria-label="Apartment building at dusk"></div>
  <div class="abs shade" style="left:0;top:0;width:386px;height:169px"></div>
  <p class="abs kicker white" style="left:18px;top:20px">Presentation Introduction</p>
  <h1 class="abs title orange" style="left:18px;top:34px;font-size:25px">Presentation Title</h1>
  <p class="abs subtitle white" style="left:18px;top:66px">The Presentation Subtitle Goes Here</p>
  <div class="abs" style="left:0;top:166px;width:386px;height:3px;background:var(--orange)"></div>
  <div class="abs footer-strip">
    <div class="brand orange"><span class="brand-mark"></span>QNRV<span class="brand-tag">Equity Partners<br>For Housing</span></div>
    <p class="contact fine"><b>Date:</b> Date Goes Here<br><b>Name:</b> Presenter Name Here</p>
  </div>
</section>

<!-- Option 2 -->
<section class="slide col-b row-1" style="background:var(--white)">
  <div class="abs" style="left:0;top:0;width:386px;height:169px;background:var(--charcoal)"></div>
  <svg class="abs" style="left:0;top:0" width="386" height="169" aria-hidden="true">
    <polygon points="0,0 150,0 70,169 0,169" fill="#333335"/>
  </svg>
  <h1 class="abs title white" style="left:176px;top:38px;font-size:24px">Presentation<br>Title</h1>
  <div class="abs" style="left:176px;top:94px;width:210px;height:20px;background:var(--orange)"></div>
  <p class="abs subtitle white" style="left:184px;top:100px">The Presentation Subtitle Goes Here</p>
  <div class="abs footer-strip">
    <div class="brand orange"><span class="brand-mark"></span>QNRV<span class="brand-tag">Equity Partners<br>For Housing</span></div>
    <p class="contact fine"><b>Date:</b> Date Goes Here<br><b>Name:</b> Presenter Name Here</p>
  </div>
</section>

<!-- Option 3 -->
<section class="slide col-a row-2">
  <div class="abs photo-dim" style="inset:0" role="img" aria-label="Apartment building, darkened"></div>
  <div class="abs" style="left:0;top:0;width:180px;height:217px;background:rgba(44,44,46,0.88)"></div>
  <div class="abs brand white" style="right:18px;top:16px"><span class="brand-mark" style="background:var(--white)"></span>QNRV</div>
  <h1 class="abs title white" style="left:18px;top:74px;font-size:22px">Presentation<br>Title</h1>
  <p class="abs subtitle white" style="left:18px;top:124px">The Presentation<br>Subtitle Goes Here</p>
  <div class="abs" style="left:18px;top:150px;width:130px;height:28px;background:var(--orange)"></div>
  <p class="abs fine white" style="left:26px;top:156px">Date: Date Goes Here<br>Name: Presenter Name Here</p>
</section>

<!-- Option 4 -->
<section class="slide col-b row-2" style="background:var(--white)">
  <div class="abs photo-day" style="left:150px;top:0;width:236px;height:217px;clip-path:polygon(20% 0,100% 0,100% 100%,0 100%)" role="img" aria-label="Apartment tower against the sky"></div>
  <svg class="abs" style="left:0;top:0" width="386" height="217" aria-hidden="true">
    <rect x="0" y="0" width="6" height="217" fill="var(--orange)"/>
    <polygon points="120,217 200,90 230,90 150,217" fill="var(--orange-soft)"/>
    <polygon points="160,217 240,90 290,90 210,217" fill="rgba(234,116,34,0.3)"/>
  </svg>
  <div class="abs brand orange" style="left:22px;top:18px;font-size:12px"><span class="brand-mark"></span>QNRV</div>
  <h1 class="abs title orange" style="left:22px;top:64px;font-size:22px">Main<br>Presentation<br>Title</h1>
  <p class="abs subtitle ink" style="left:22px;top:140px">The Presentation<br>Subtitle Goes Here</p>
</section>

<!-- Option 5 -->
<section class="slide col-a row-3" style="background:var(--orange)">
  <div class="abs" style="inset:0;background:linear-gradient(120deg, rgba(255,255,255,0.08) 0%, rgba(0,0,0,0.08) 100%)" role="img" aria-label="Faint apartment building outline"></div>
  <div class="abs brand white" style="left:0;right:0;top:14px;justify-content:center;font-size:12px"><span class="brand-mark" style="background:var(--white)"></span>QNRV</div>
  <div class="abs" style="left:96px;top:48px;width:194px;height:132px;background:var(--charcoal)"></div>
  <h1 class="abs title white" style="left:110px;top:60px;font-size:22px">Presentation<br>Title</h1>
  <p class="abs subtitle white" style="left:110px;top:112px">The Presentation<br>Subtitle Goes Here</p>
  <div class="abs info-box fine" style="left:110px;top:140px;width:130px">Date: Date Goes Here<br>Name: Presenter Name Here</div>
</section>

<!-- Option 6 -->
<section class="slide col-b row-3" style="background:var(--orange)">
  <div class="abs" style="inset:0;background:linear-gradient(300deg, rgba(0,0,0,0.1) 0%, rgba(255,255,255,0.06) 100%)" role="img" aria-label="Faint apartment building outline"></div>
  <div class="abs" style="left:70px;top:34px;width:246px;height:150px;background:var(--charcoal)"></div>
  <h1 class="abs title orange" style="left:88px;top:50px;font-size:24px">Presentation<br>Title</h1>
  <p class="abs subtitle white" style="left:88px;top:108px">The Presentation Subtitle Goes Here</p>
  <div class="abs" style="left:88px;top:130px;width:228px;height:3px;background:var(--orange)"></div>
  <p class="abs fine white" style="left:88px;top:142px">Date: Date Goes Here<br>Name: Presenter Name Here</p>
</section>

<!-- Option 7 -->
<section class="slide col-a row-4">
  <div class="abs photo-night" style="inset:0" role="img" aria-label="Apartment building at night"></div>
  <div class="abs" style="inset:0;background:rgba(28,37,54,0.55)"></div>
  <div class="abs brand white" style="left:0;right:0;top:14px;justify-content:center;font-size:12px"><span class="brand-mark"></span>QNRV</div>
  <p class="abs kicker white" style="left:0;right:0;top:44px;text-align:center">Presentation Introduction</p>
  <h1 class="abs title orange" style="left:0;right:0;top:58px;text-align:center;font-size:26px">Presentation Title</h1>
  <p class="abs subtitle white" style="left:0;right:0;top:94px;text-align:center">The Presentation Subtitle Goes Here</p>
  <div class="abs info-box fine" style="left:128px;top:118px;width:130px;text-align:center">Date: Date Goes Here<br>Name: Presenter Name Here</div>
</section>

<!-- Option 8 -->
<section class="slide col-b row-4">
  <div class="abs photo-night" style="inset:0" role="img" aria-label="Apartment building at night"></div>
  <div class="abs" style="inset:0;background:rgba(20,26,38,0.6)"></div>
  <div class="abs brand white" style="left:0;right:0;top:16px;justify-content:center;font-size:12px"><span class="brand-mark"></span>QNRV</div>
  <h1 class="abs title orange" style="left:0;right:0;top:76px;text-align:center;font-size:26px">Presentation Title</h1>
  <p class="abs subtitle white" style="left:0;right:0;top:112px;text-align:center">The Presentation Subtitle Goes Here</p>
</section>

</body>
</html>
```